Briar Hollow

Need a site for a cbd dispensary texas theme. We sell all federal and legal hemp products

Target Market(s)

Cbd and other hemp derivatives

Industry/Entity Type

Hemp derivatives

Coding

Coded - Design and coding required

Number of Pages Required

3 page

Font styles to use
Sans Serif

Colors
0094D4
00A9DD
6FCCEA
C7EBF8
E9F6FB

Requirements
Must have
• Integration for bigcommerce shopping
Nice to have
• Easy layout for shopping

```html
<!DOCTYPE html>
<html lang="en">
<head>
<meta charset="utf-8">
<title>Briar Hollow – Hemp Dispensary</title>
<link rel="stylesheet" href="https://fonts.googleapis.com/css2?family=Roboto+Condensed:wght@400;700&family=Roboto:ital,wght@0,400;0,500;0,700;1,400&display=swap">
<style>
:root{
  --blue:#00A9DD;
  --blue-dark:#0094D4;
  --blue-mid:#6FCCEA;
  --blue-pale:#C7EBF8;
  --blue-ice:#E9F6FB;
  --ink:#111;
  --text:#333;
  --muted:#777;
  --white:#fff;
  --black:#050505;
}
*{box-sizing:border-box;margin:0;padding:0}
html,body{width:1200px;height:4938px;overflow:hidden}
body{position:relative;font-family:"Roboto",Arial,sans-serif;color:var(--text);background:var(--white)}
.abs{position:absolute}
.cond{font-family:"Roboto Condensed","Arial Narrow",sans-serif}

/* top bar */
.topbar{left:0;top:0;width:1200px;height:52px;background:var(--black);color:var(--blue);font-size:15px;font-weight:700}
.topbar .currency{left:111px;top:16px;display:flex;align-items:center;gap:6px}
.flag{width:40px;height:22px;background:linear-gradient(#2a4a9a 0 50%,#d33 50% 60%,#fff 60% 70%,#d33 70% 80%,#fff 80% 90%,#d33 90%);border:1px solid #fff}
.topbar .links{right:110px;top:16px;display:flex;gap:26px}

/* header */
.header{left:0;top:52px;width:1200px;height:92px;background:var(--white)}
.logo{left:63px;top:52px;width:265px;height:149px;background:var(--white);z-index:3;display:flex;align-items:center;justify-content:center;gap:10px}
.logo .mark{width:20px;height:20px;border-radius:50%;background:var(--blue)}
.logo .name{font-family:"Roboto Condensed",sans-serif;font-weight:700;font-size:40px;color:var(--blue);line-height:1}
.nav{top:88px;left:373px;display:flex;gap:0;font-size:13px;font-weight:700;color:var(--ink)}
.nav span{position:absolute;white-space:nowrap}
.nav-caret{left:380px;top:130px;width:0;height:0;border-left:11px solid transparent;border-right:11px solid transparent;border-bottom:15px solid var(--blue)}
.hicon{width:38px;height:38px;border-radius:50%;background:var(--blue);top:79px;display:flex;align-items:center;justify-content:center}

/* hero */
.hero{left:0;top:144px;width:1200px;height:671px;background:linear-gradient(100deg,#d9d6cf 0%,#c8c1b0 35%,#9a8c60 55%,#4f6a2f 80%,#2f4a20 100%)}
.hero-box{left:109px;top:362px;width:455px;height:213px;background:var(--blue);color:var(--white);padding:24px 28px}
.hero-box h1{font-family:"Roboto Condensed",sans-serif;font-size:48px;font-weight:700;line-height:1.05}
.hero-box p{font-size:13px;line-height:1.5;margin-top:12px;width:400px}
.btn-white{display:inline-block;margin-top:18px;background:var(--white);color:var(--blue);font-size:12px;font-weight:700;padding:14px 26px;border-radius:5px}
.round-arrow{width:48px;height:48px;border-radius:50%;display:flex;align-items:center;justify-content:center}
.hero .dots{left:110px;top:602px;display:flex;gap:6px}
.hero .dots i{display:block;width:12px;height:12px;border-radius:50%;background:#fff}
.hero .dots i:first-child{background:var(--blue);width:16px;height:16px;margin-top:-2px}

/* categories */
.tile{overflow:hidden}
.tile .frame{position:absolute;left:18px;top:18px;right:18px;bottom:18px;border:2px solid #fff;display:flex;flex-direction:column;align-items:center;justify-content:center;color:#fff;font-family:"Roboto Condensed",sans-serif;font-weight:700;font-size:16px}
.btn-outline{margin-top:14px;border:2px solid #fff;border-radius:5px;padding:10px 22px;font-size:12px}

/* section titles */
.sec-title{left:0;width:1200px;text-align:center;font-family:"Roboto Condensed",sans-serif;font-weight:700;font-size:52px;color:var(--ink);line-height:1}

/* products */
.featured-bg{left:0;top:1399px;width:1200px;height:1068px;background:linear-gradient(180deg,#f6f4ef 0%,#fbfaf7 40%,#efe9df 100%)}
.pcard{width:311px;height:360px;background:var(--white);box-shadow:0 2px 10px rgba(0,0,0,.08);overflow:hidden}
.pcard .shot{position:absolute;left:105px;top:14px;width:100px;height:215px;border-radius:8px}
.pcard .pname{position:absolute;top:246px;width:100%;text-align:center;font-size:19px;color:var(--ink)}
.pcard .price{position:absolute;top:282px;width:100%;text-align:center;font-size:20px;font-weight:700;color:var(--blue)}
.cart-tab{position:absolute;left:104px;bottom:-52px;width:104px;height:104px;border-radius:50%;background:var(--blue)}
.cart-tab svg{position:absolute;left:40px;top:16px}
.new-band{left:0;top:2467px;width:1200px;height:629px;background:var(--blue)}
.ncard{width:311px;height:360px;background:var(--white)}
.ncard .shot{position:absolute;left:45px;top:25px;width:220px;height:225px;border-radius:8px}
.ncard .pname{position:absolute;left:45px;top:270px;font-size:19px;color:var(--ink)}
.ncard .price{position:absolute;left:45px;top:306px;font-size:20px;font-weight:700;color:var(--blue)}

/* blog */
.bcard{width:236px;height:429px;background:var(--white);box-shadow:0 2px 10px rgba(0,0,0,.1)}
.bcard .img{position:absolute;left:0;top:0;width:236px;height:272px}
.bcard .date{position:absolute;left:0;top:246px;width:100%;text-align:center;font-size:12px;color:var(--blue);font-weight:500}
.bcard h3{position:absolute;top:290px;width:100%;text-align:center;font-family:"Roboto Condensed",sans-serif;font-size:18px;line-height:1.45;color:var(--ink);font-weight:700}
.bcard .more{position:absolute;top:354px;left:57px;width:122px;height:44px;background:var(--blue);color:#fff;border-radius:5px;font-size:12px;font-weight:700;display:flex;align-items:center;justify-content:center;gap:5px}

/* testimonials */
.tcard{width:478px;height:234px;background:var(--white);box-shadow:0 2px 12px rgba(0,0,0,.12);padding:30px 40px 0 42px}
.tcard p{font-size:13.5px;font-style:italic;line-height:1.65;color:#777}
.avatar{width:120px;height:120px;border-radius:50%;border:3px solid #fff;background:linear-gradient(160deg,#c9d6e3,#8aa0b5)}
.who{font-family:"Roboto Condensed",sans-serif;font-size:22px;font-weight:700;color:var(--ink)}
.who small{font-family:"Roboto",sans-serif;font-size:13px;font-weight:400;color:#888;margin-left:14px}

/* newsletter band */
.news-band{left:0;top:4279px;width:1200px;height:205px;background:linear-gradient(90deg,var(--blue-dark),var(--blue))}
.news-band h2{position:absolute;left:111px;top:82px;font-family:"Roboto Condensed",sans-serif;font-size:34px;color:#fff;font-weight:700}
.news-form{position:absolute;left:558px;top:72px;width:529px;height:62px;background:#fff;border:3px solid #fff;display:flex}
.news-form span{flex:1;padding:18px 28px;font-size:13px;color:#777}
.news-form b{width:165px;background:var(--blue);color:#fff;font-size:13px;display:flex;align-items:center;justify-content:center}

/* footer */
.footer{left:0;top:4484px;width:1200px;height:454px;background:var(--black);color:#fff}
.footer h4{position:absolute;top:88px;font-family:"Roboto Condensed",sans-serif;font-size:20px;color:var(--blue);font-weight:700}
.footer ul{position:absolute;list-style:none;font-size:14px;line-height:30px}
.f-contact{position:absolute;left:111px;font-size:14px;line-height:20px;display:flex;gap:18px}
.f-contact svg{flex:none;margin-top:2px}
.footer .mini{position:absolute;left:807px;top:150px;width:290px;font-size:14px;line-height:24px}
.footer .mini-in{position:absolute;left:807px;top:232px;width:280px;height:44px;border:1px solid #fff;font-size:14px;padding:12px 14px}
.footer .rule{position:absolute;left:111px;top:366px;width:978px;height:1px;background:#333}
.footer .socials{position:absolute;left:111px;top:397px;display:flex;gap:14px}
.footer .socials i{display:block;width:11px;height:11px;border-radius:50%;background:#fff}
.footer .copy{position:absolute;right:111px;top:394px;font-size:13px}
</style>
</head>
<body>

<!-- top bar -->
<div class="abs topbar">
  <div class="abs currency"><span class="flag" role="img" aria-label="US flag"></span>USD <svg width="10" height="8" viewBox="0 0 10 8"><path d="M1 2l4 4 4-4" stroke="#00A9DD" stroke-width="2" fill="none"/></svg></div>
  <div class="abs links">
    <span><svg width="14" height="12" viewBox="0 0 14 12"><path d="M7 12L1 6a3.3 3.3 0 0 1 6-4 3.3 3.3 0 0 1 6 4z" fill="#00A9DD"/></svg> Wish lists</span>
    <span><svg width="13" height="13" viewBox="0 0 13 13"><path d="M3 0l2 3-1.5 2a7 7 0 0 0 4.5 4.5L10 8l3 2-1 3C6 13 0 7 0 1z" fill="#00A9DD"/></svg> Call us : +1 555 014 2290</span>
  </div>
</div>

<!-- header -->
<div class="abs header"></div>
<div class="abs logo"><span class="mark"></span><span class="name">Briar Hollow</span></div>
<nav class="abs nav" style="left:0">
  <span style="left:373px">SHOP</span><span style="left:437px">BLOG</span><span style="left:498px">ABOUT</span><span style="left:571px">FEATURES</span><span style="left:666px">REVIEWS</span><span style="left:753px">SUPPORT</span><span style="left:843px">EPIC EXTRAS</span>
</nav>
<div class="abs nav-caret"></div>
<div class="abs hicon" style="left:964px"><svg width="16" height="16" viewBox="0 0 16 16"><circle cx="6.5" cy="6.5" r="4.5" stroke="#fff" stroke-width="2" fill="none"/><path d="M10 10l4 4" stroke="#fff" stroke-width="2.5"/></svg></div>
<div class="abs hicon" style="left:1008px"><svg width="14" height="16" viewBox="0 0 14 16"><circle cx="7" cy="4.5" r="3.5" fill="#fff"/><path d="M0 16a7 6 0 0 1 14 0z" fill="#fff"/></svg></div>
<div class="abs hicon" style="left:1051px"><svg width="17" height="15" viewBox="0 0 17 15"><path d="M0 1h3l2 8h9l2-6H4" stroke="#fff" stroke-width="2" fill="none"/><circle cx="6" cy="13" r="1.6" fill="#fff"/><circle cx="13" cy="13" r="1.6" fill="#fff"/></svg></div>

<!-- hero -->
<section class="abs hero" role="img" aria-label="Dropper releasing golden hemp oil into a glass bottle beside hemp leaves and a wooden spoon of seeds">
  <div class="abs round-arrow" style="left:32px;top:307px;background:rgba(90,90,90,.75)"><svg width="12" height="14" viewBox="0 0 12 14"><path d="M8 2L3 7l5 5" stroke="#fff" stroke-width="2" fill="none"/></svg></div>
  <div class="abs round-arrow" style="left:1120px;top:307px"><svg width="12" height="14" viewBox="0 0 12 14"><path d="M4 2l5 5-5 5" stroke="#fff" stroke-width="2" fill="none"/></svg></div>
  <div class="abs dots"><i></i><i></i><i></i><i></i></div>
</section>
<div class="abs hero-box">
  <h1>Briar Hollow</h1>
  <p>Lorem ipsum dolor sit amet, consectetur adipiscing elit, sed do or incididunt ut labore et dolore magna aliqua.</p>
  <span class="btn-white">SHOP NOW</span>
</div>

<!-- category tiles -->
<div class="abs tile" style="left:10px;top:826px;width:584px;height:282px;background:linear-gradient(135deg,#3b2f22,#6b5a3c 55%,#2d3a22)" role="img" aria-label="Bottles of hemp oil with a leaf on a dark table">
  <div class="frame">Lorem ipsum dolor sit amet<span class="btn-outline">VIEW CATEGORY</span></div></div>
<div class="abs tile" style="left:10px;top:1118px;width:287px;height:281px;background:linear-gradient(160deg,#4a4336,#8b7d60 60%,#5a4a33)" role="img" aria-label="Jar of hemp seeds on a burlap sack">
  <div class="frame">Lorem ipsum dolor sit amet<span class="btn-outline">VIEW CATEGORY</span></div></div>
<div class="abs tile" style="left:309px;top:1118px;width:285px;height:281px;background:linear-gradient(160deg,#6f7a4a,#a7a27a 55%,#8e7a5a)" role="img" aria-label="Hands holding a dropper bottle of hemp oil">
  <div class="frame">Lorem ipsum dolor sit amet<span class="btn-outline">VIEW CATEGORY</span></div></div>
<div class="abs tile" style="left:606px;top:826px;width:584px;height:573px;background:linear-gradient(160deg,#5a4334,#8a6b55 45%,#4b3326)" role="img" aria-label="Hemp leaf and oil bottle on a rustic wooden table">
  <div class="frame">Lorem ipsum dolor sit amet<span class="btn-outline">VIEW CATEGORY</span></div></div>

<!-- featured products -->
<div class="abs featured-bg" role="img" aria-label="Faded background of oil bottles and hemp seeds"></div>
<h2 class="abs sec-title" style="top:1496px">FEATURED PRODUCTS</h2>
<p class="abs" style="left:0;width:1200px;top:1563px;text-align:center;font-size:15px;color:#444">Lorem ipsum dolor sit amet, consectetur adipiscing elit, sed do eiusmod tempor</p>

<div class="abs round-arrow" style="left:32px;top:1964px;background:#777"><svg width="12" height="14" viewBox="0 0 12 14"><path d="M8 2L3 7l5 5" stroke="#fff" stroke-width="2" fill="none"/></svg></div>
<div class="abs round-arrow" style="left:1120px;top:1964px;background:#777"><svg width="12" height="14" viewBox="0 0 12 14"><path d="M4 2l5 5-5 5" stroke="#fff" stroke-width="2" fill="none"/></svg></div>

<div class="abs pcard" style="left:111px;top:1616px"><div class="shot" role="img" aria-label="Clear dropper bottle of golden oil" style="background:linear-gradient(#e9e9e9,#e6c85a)"></div><div class="pname">Nemo enim ipsam</div><div class="price">$25.00</div><div class="cart-tab"><svg width="24" height="22" viewBox="0 0 17 15"><path d="M0 1h3l2 8h9l2-6H4" stroke="#fff" stroke-width="2" fill="none"/><circle cx="6" cy="13" r="1.6" fill="#fff"/><circle cx="13" cy="13" r="1.6" fill="#fff"/></svg></div></div>
<div class="abs pcard" style="left:445px;top:1616px"><div class="shot" role="img" aria-label="Black-capped dropper bottle of yellow oil" style="background:linear-gradient(#222 0 35%,#f0d23a 35%)"></div><div class="pname">Nemo enim ipsam</div><div class="price">$25.00</div><div class="cart-tab"><svg width="24" height="22" viewBox="0 0 17 15"><path d="M0 1h3l2 8h9l2-6H4" stroke="#fff" stroke-width="2" fill="none"/><circle cx="6" cy="13" r="1.6" fill="#fff"/><circle cx="13" cy="13" r="1.6" fill="#fff"/></svg></div></div>
<div class="abs pcard" style="left:776px;top:1616px"><div class="shot" role="img" aria-label="Amber dropper bottle with blue cap" style="background:linear-gradient(#2f7fd6 0 30%,#ddd 30% 40%,#b4661f 40%)"></div><div class="pname">Nemo enim ipsam</div><div class="price">$25.00</div><div class="cart-tab"><svg width="24" height="22" viewBox="0 0 17 15"><path d="M0 1h3l2 8h9l2-6H4" stroke="#fff" stroke-width="2" fill="none"/><circle cx="6" cy="13" r="1.6" fill="#fff"/><circle cx="13" cy="13" r="1.6" fill="#fff"/></svg></div></div>
<div class="abs pcard" style="left:111px;top:2003px"><div class="shot" role="img" aria-label="White nasal drop bottle" style="background:linear-gradient(#eee,#d8d8d8 60%,#a8cf8a)"></div><div class="pname">Nemo enim ipsam</div><div class="price">$25.00</div><div class="cart-tab"><svg width="24" height="22" viewBox="0 0 17 15"><path d="M0 1h3l2 8h9l2-6H4" stroke="#fff" stroke-width="2" fill="none"/><circle cx="6" cy="13" r="1.6" fill="#fff"/><circle cx="13" cy="13" r="1.6" fill="#fff"/></svg></div></div>
<div class="abs pcard" style="left:445px;top:2003px"><div class="shot" role="img" aria-label="Dark red dropper bottle" style="background:linear-gradient(#e5e5e5 0 30%,#8a1c1c 30%)"></div><div class="pname">Nemo enim ipsam</div><div class="price">$25.00</div><div class="cart-tab"><svg width="24" height="22" viewBox="0 0 17 15"><path d="M0 1h3l2 8h9l2-6H4" stroke="#fff" stroke-width="2" fill="none"/><circle cx="6" cy="13" r="1.6" fill="#fff"/><circle cx="13" cy="13" r="1.6" fill="#fff"/></svg></div></div>
<div class="abs pcard" style="left:776px;top:2003px"><div class="shot" role="img" aria-label="Orange dropper bottle with white cap" style="background:linear-gradient(#e5e5e5 0 32%,#c9551e 32%)"></div><div class="pname">Nemo enim ipsam</div><div class="price">$25.00</div><div class="cart-tab"><svg width="24" height="22" viewBox="0 0 17 15"><path d="M0 1h3l2 8h9l2-6H4" stroke="#fff" stroke-width="2" fill="none"/><circle cx="6" cy="13" r="1.6" fill="#fff"/><circle cx="13" cy="13" r="1.6" fill="#fff"/></svg></div></div>

<!-- new products -->
<section class="abs new-band">
  <h2 class="abs sec-title" style="top:88px;color:#fff">NEW PRODUCTS</h2>
  <div class="abs" style="left:42px;top:340px"><svg width="30" height="30" viewBox="0 0 30 30"><circle cx="15" cy="15" r="14" fill="#fff"/><path d="M17 8l-7 7 7 7M10 15h11" stroke="#00A9DD" stroke-width="3" fill="none"/></svg></div>
  <div class="abs" style="left:1129px;top:340px"><svg width="30" height="30" viewBox="0 0 30 30"><circle cx="15" cy="15" r="14" fill="#fff"/><path d="M13 8l7 7-7 7M20 15H9" stroke="#00A9DD" stroke-width="3" fill="none"/></svg></div>
  <div class="abs ncard" style="left:111px;top:171px"><div class="shot" role="img" aria-label="White hemp oil bottle with leaf" style="background:linear-gradient(#f4f4f4 0 55%,#cfe3b8 55%,#3f8a2a)"></div><div class="pname">Nemo enim ipsam</div><div class="price">$25.00</div></div>
  <div class="abs ncard" style="left:445px;top:171px"><div class="shot" role="img" aria-label="Clear hemp oil bottle with leaf" style="background:linear-gradient(#f4f4f4 0 55%,#d4ecd9 55%,#3f8a2a)"></div><div class="pname">Nemo enim ipsam</div><div class="price">$25.00</div></div>
  <div class="abs ncard" style="left:776px;top:171px"><div class="shot" role="img" aria-label="Black hemp oil bottle with leaves" style="background:linear-gradient(#2a2a2a 0 60%,#3f8a2a)"></div><div class="pname">Nemo enim ipsam</div><div class="price">$25.00</div></div>
</section>

<!-- blog -->
<h2 class="abs sec-title" style="top:3193px">OUR LATEST BLOG</h2>
<div class="abs" style="left:41px;top:3420px"><svg width="30" height="30" viewBox="0 0 30 30"><circle cx="15" cy="15" r="14" fill="#111"/><path d="M17 8l-7 7 7 7M10 15h11" stroke="#fff" stroke-width="3" fill="none"/></svg></div>
<div class="abs" style="left:1128px;top:3420px"><svg width="30" height="30" viewBox="0 0 30 30"><circle cx="15" cy="15" r="14" fill="#111"/><path d="M13 8l7 7-7 7M20 15H9" stroke="#fff" stroke-width="3" fill="none"/></svg></div>

<article class="abs bcard" style="left:109px;top:3265px"><div class="img" role="img" aria-label="Droppers over oil bottles on soil" style="background:linear-gradient(#8a8c5a,#b99a2e 60%,#4a3a22)"></div><div class="date">&#9635; Jan 20th,2021</div><h3>Lorem ipsum dolor sit<br>amet, consectetur</h3><span class="more">READ MORE <svg width="11" height="11" viewBox="0 0 11 11"><circle cx="5.5" cy="5.5" r="5.5" fill="#fff"/><path d="M4 3l3 2.5L4 8" stroke="#00A9DD" stroke-width="1.6" fill="none"/></svg></span></article>
<article class="abs bcard" style="left:357px;top:3265px"><div class="img" role="img" aria-label="Gloved hand holding a dropper bottle" style="background:linear-gradient(#b9c4cc,#e4e6e4 50%,#c9b25a)"></div><div class="date">&#9635; Jan 20th,2021</div><h3>Lorem ipsum dolor sit<br>amet, consectetur</h3><span class="more">READ MORE <svg width="11" height="11" viewBox="0 0 11 11"><circle cx="5.5" cy="5.5" r="5.5" fill="#fff"/><path d="M4 3l3 2.5L4 8" stroke="#00A9DD" stroke-width="1.6" fill="none"/></svg></span></article>
<article class="abs bcard" style="left:606px;top:3265px"><div class="img" role="img" aria-label="Jar of dried hemp flower with a spoon" style="background:linear-gradient(#6d8aa8,#a9b4b8 50%,#8b6b45)"></div><div class="date">&#9635; Jan 20th,2021</div><h3>Lorem ipsum dolor sit<br>amet, consectetur</h3><span class="more">READ MORE <svg width="11" height="11" viewBox="0 0 11 11"><circle cx="5.5" cy="5.5" r="5.5" fill="#fff"/><path d="M4 3l3 2.5L4 8" stroke="#00A9DD" stroke-width="1.6" fill="none"/></svg></span></article>
<article class="abs bcard" style="left:853px;top:3265px"><div class="img" role="img" aria-label="Shop owner at a hemp store counter" style="background:linear-gradient(#d8d2c6,#efe9df 50%,#b8a58a)"></div><div class="date">&#9635; Jan 20th,2021</div><h3>Lorem ipsum dolor sit<br>amet, consectetur</h3><span class="more">READ MORE <svg width="11" height="11" viewBox="0 0 11 11"><circle cx="5.5" cy="5.5" r="5.5" fill="#fff"/><path d="M4 3l3 2.5L4 8" stroke="#00A9DD" stroke-width="1.6" fill="none"/></svg></span></article>

<!-- testimonials -->
<h2 class="abs sec-title" style="top:3791px">WHAT OUR CUSTOMERS ARE SAYING</h2>
<div class="abs" style="left:66px;top:3976px"><svg width="60" height="22" viewBox="0 0 60 22"><path d="M58 11H3M12 2L2 11l10 9" stroke="#111" stroke-width="2" fill="none"/></svg></div>
<div class="abs" style="left:1072px;top:3976px"><svg width="60" height="22" viewBox="0 0 60 22"><path d="M2 11h55M48 2l10 9-10 9" stroke="#111" stroke-width="2" fill="none"/></svg></div>

<div class="abs tcard" style="left:109px;top:3878px"><p>"Lorem ipsum dolor sit amet, consectetur adipiscing elit, sed do eiusmod tempor incididunt ut labore et dolore magna aliqua. Ut enim ad minim veniam, quis nostrud exercitation ullamco laboris nisi ut aliquip ex ea commodo consequat. Duis aute irure dolor in reprehenderit in voluptate velit esse cillum dolore eu fugiat nulla pariatur."</p></div>
<div class="abs tcard" style="left:610px;top:3878px"><p>"Lorem ipsum dolor sit amet, consectetur adipiscing elit, sed do eiusmod tempor incididunt ut labore et dolore magna aliqua. Ut enim ad minim veniam, quis nostrud exercitation ullamco laboris nisi ut aliquip ex ea commodo consequat. Duis aute irure dolor in reprehenderit in voluptate velit esse cillum dolore eu fugiat nulla pariatur."</p></div>
<div class="abs avatar" style="left:151px;top:4054px" role="img" aria-label="Customer portrait"></div>
<div class="abs avatar" style="left:653px;top:4054px" role="img" aria-label="Customer portrait"></div>
<div class="abs who" style="left:295px;top:4064px">Dana Reyes<small>Company name</small></div>
<div class="abs who" style="left:796px;top:4064px">Dana Reyes<small>Company name</small></div>

<!-- newsletter band -->
<section class="abs news-band" role="img" aria-label="Blue band with faint hemp leaf silhouettes">
  <h2>SUBSCRIBE OUR NEWSLETTER</h2>
  <div class="news-form"><span>Email address</span><b>SUBSCIBE</b></div>
</section>

<!-- footer -->
<footer class="abs footer">
  <h4 style="left:111px">Contact us</h4>
  <h4 style="left:387px">Quick link</h4>
  <h4 style="left:608px">Help</h4>
  <h4 style="left:807px">Sign up for our newsletter</h4>

  <div class="f-contact" style="top:152px"><svg width="9" height="13" viewBox="0 0 9 13"><path d="M4.5 13S0 7 0 4.5a4.5 4.5 0 0 1 9 0C9 7 4.5 13 4.5 13z" fill="#00A9DD"/><circle cx="4.5" cy="4.5" r="1.6" fill="#050505"/></svg><span>48 Cedar Mill Rd,<br>Fairhaven, TX 75012</span></div>
  <div class="f-contact" style="top:208px"><svg width="12" height="12" viewBox="0 0 13 13"><path d="M3 0l2 3-1.5 2a7 7 0 0 0 4.5 4.5L10 8l3 2-1 3C6 13 0 7 0 1z" fill="#00A9DD"/></svg><span>555.203.4410</span></div>
  <div class="f-contact" style="top:246px"><svg width="13" height="12" viewBox="0 0 13 12"><rect x="0" y="3" width="13" height="9" fill="#00A9DD"/><rect x="3" y="0" width="7" height="4" fill="#00A9DD"/></svg><span>555.203.4412</span></div>

  <ul style="left:390px;top:132px"><li>Home</li><li>About us</li><li>Shop</li><li>Blog</li><li>Contact Us</li></ul>
  <ul style="left:611px;top:132px"><li>Terms &amp; Condtions</li><li>Privacy</li><li>Policy</li><li>About Us</li><li>Support</li></ul>

  <p class="mini">Lorem ipsum dolor sit amet, consectetur adipiscing elit, sed do eiusmod tempor incididunt ut labore et dolore magna</p>
  <div class="mini-in">Enter your email
    <svg style="position:absolute;right:12px;top:14px" width="16" height="12" viewBox="0 0 16 12"><rect x="1" y="1" width="14" height="10" stroke="#fff" stroke-width="1.5" fill="none"/><path d="M1 1l7 6 7-6" stroke="#fff" stroke-width="1.5" fill="none"/></svg></div>

  <div class="rule"></div>
  <div class="socials"><i></i><i></i><i></i><i></i></div>
  <div class="copy">© Copyrights 2021 Company Name &nbsp;|&nbsp; All Rights Reserved</div>
</footer>

</body>
</html>
```